Zielgruppe
Wir sind eine Imkerei mit angeschlossenem Lehrgarten. Unsere Produktpalette umfasst selbst hergestellte Imkereiprodukte aller Art (Honig, Bienenwachskerzen, Propolis, Pollen, Met). Unsere Zielgruppe sind solvente, umweltbewusste Konsumenten mit dem Sinn für nachhaltig und regional produzierte Waren.
Aufgabenstellung
- Das Etikett soll maximal die Logo-Farben nutzen (weiß, schwarz, gelb), evtl. mit goldenen Akzenten.
- Logo 'Imkerei Fam. Halvers' integrieren
- Ein gleich aussehendes Grundetikett für mehrere Sorten
- Honigname 'Dünenglanz' + Sortenbezeichnung (Rapshonig, Frühtrachthonig, Sommertrachthonig), zusätzlich ein 'Leeretikett' zum Einstempeln von Sondersorten
- Optische Elemente gerne Waben und/oder Regionales (Friesland, Jadebusen, Nordsee)
- Wir erweitern Stück für Stück unser Sortiment, daher soll das Grunddesign später auf Etiketten für zum Beispiel Met, Seife und Bonbons auszuweiten sein.
- Etiketten in 3 verschiedenen Größen nutzbar (500g, 250g, 50g)
- Pflichtangaben auf Honigetiketten: Deutscher Honig/ Honig aus Deutschland, Füllmenge (Schriftgröße mind. 4 mm Höhe), Hersteller/ Name und Anschrift des Imkers (zunächst Platzhalter nutzen, Daten werden im Verlauf übermittelt), Platz für Datumsstempel (MHD), Lagerbedingung (kühl, trocken und dunkel lagern)
- Das Etikett soll einen Gewährverschluss haben, obenauf das leere Feld für den Datumsstempel
- Das Honigglas hat einen goldenen Deep Twist Off Deckel

```html
<!DOCTYPE html>
<html lang="de">
<head>
<meta charset="utf-8">
<title>Dünenglanz Frühtracht Honig – Etikett</title>
<link href="https://fonts.googleapis.com/css2?family=Amatic+SC:wght@700&family=Montserrat:wght@800&family=Yellowtail&display=block" rel="stylesheet">
<style>
  :root{
    --paper:#f1efe9;
    --paper-shade:#e9e6df;
    --ink:#232323;
    --line:#555555;
    --honey:#f2c230;
    --honey-soft:#f6d77a;
    --honey-text:#f3b51b;
    --grey:#a9a9a9;
    --grey-dark:#7a7a7a;
  }
  *{margin:0;padding:0;box-sizing:border-box}
  html,body{width:954px;height:1200px;overflow:hidden;background:var(--paper)}
  .label{
    position:relative;width:954px;height:1200px;overflow:hidden;
    background:radial-gradient(ellipse at 40% 30%, var(--paper) 0%, var(--paper-shade) 100%);
    color:var(--ink);
  }
  .label svg.backdrop{position:absolute;inset:0;width:954px;height:1200px}
  .hand{font-family:'Amatic SC',cursive;font-weight:700;line-height:1;text-transform:uppercase}
  .storage{
    position:absolute;left:475px;top:532px;
    transform:translate(-50%,-50%) rotate(-90deg);
    white-space:nowrap;font-size:29px;
  }
  .maker{
    position:absolute;left:90px;top:960px;
    transform:translate(-50%,-50%) rotate(-90deg);
    white-space:nowrap;font-size:31px;text-align:center;line-height:1.25;
  }
  .origin{
    position:absolute;left:393px;width:240px;top:816px;
    text-align:center;font-size:46px;white-space:nowrap;
  }
  .name{
    position:absolute;left:0;width:954px;top:828px;padding-left:8px;text-align:center;
    font-family:'Yellowtail',cursive;font-weight:400;font-size:104px;line-height:1.1;
    color:var(--honey-text);text-shadow:4px 4px 0 var(--ink);
  }
  .variety{
    position:absolute;left:0;width:954px;top:990px;padding-left:0;text-align:center;
    font-family:'Montserrat',sans-serif;font-weight:800;font-size:60px;line-height:1.1;
  }
  .best-before{
    position:absolute;left:766px;top:766px;width:145px;
    font-size:40px;line-height:1.32;white-space:nowrap;
  }
  .weight{
    position:absolute;left:766px;top:1100px;line-height:1;
    font-family:'Montserrat',sans-serif;font-weight:800;font-size:47px;word-spacing:-6px;
  }
  .brand{
    position:absolute;left:379px;top:91px;width:192px;height:192px;
    border:2px solid var(--line);border-radius:50%;
    display:flex;align-items:center;justify-content:center;text-align:center;
    font-family:'Amatic SC',cursive;font-weight:700;font-size:38px;line-height:1.05;color:var(--ink);
  }
</style>
</head>
<body>
<div class="label">
  <svg class="backdrop" viewBox="0 0 954 1200" aria-hidden="true">
    <defs>
      <polygon id="hex" points="1,0 0.5,0.866 -0.5,0.866 -1,0 -0.5,-0.866 0.5,-0.866"/>
    </defs>
    <g class="honeycomb">
      <use href="#hex" fill="var(--honey-soft)" opacity=".75" transform="translate(615 812) rotate(-10) scale(155)"/>
      <use href="#hex" fill="var(--grey)" opacity=".45" transform="translate(400 942) rotate(-10) scale(135)"/>
      <use href="#hex" fill="var(--grey)" opacity=".8" transform="translate(850 850) rotate(-10) scale(155)"/>
      <use href="#hex" fill="var(--honey)" transform="translate(1030 660) rotate(-10) scale(155)"/>
      <use href="#hex" fill="var(--honey-soft)" opacity=".9" transform="translate(672 1070) rotate(-10) scale(150)"/>
      <use href="#hex" fill="var(--honey)" transform="translate(915 1095) rotate(-10) scale(150)"/>
      <use href="#hex" fill="var(--grey-dark)" transform="translate(705 1268) rotate(-10) scale(150)"/>
    </g>
    <path class="die-line" d="M380,19 L569,19 L662,185 L569,349 L569,736 L935,736 L935,1178 L14,1178 L14,736 L380,736 L380,349 L288,185 Z"
      fill="none" stroke="var(--line)" stroke-width="2.5"/>
  </svg>

  <div class="brand">Imkerei<br>Fam. Halvers</div>

  <div class="storage hand">Kühl, trocken und dunkel lagern</div>
  <div class="maker hand">Imkerei Familie Halvers GmbH<br>Musterstraße 1, 12345 Musterhausen</div>

  <div class="origin hand">Deutscher Honig</div>
  <div class="name">Dünenglanz</div>
  <div class="variety">FRÜHTRACHT<br>HONIG</div>

  <div class="best-before hand">Mindesteens<br>haltbar bis:</div>
  <div class="weight">250 G</div>
</div>
</body>
</html>
```